Harrowmere Logistics, Project

Company Profile
Harrowmere Logistics Sdn Bhd is a well established and experienced freight forwarder in Kuala Lumpur, Malaysia. We specialize in air and sea forwarding, Custom Brokerage and regulatory compliance services, inland transportation,
overseas freighting and warehousing and distribution management. With our dedicated qualified and experienced professionals, we are fully committed to serving our clients.

Our Mission
Based on the motto “Quick, Reliable and Polite”, Harrowmere Logistics is dedicated to upholding the following three points corporate philosophy:
1. Adhering to the principle that “the customer always comes first”.
2. Contributing to the development of the local community.
3. Making it our duty to be responsible and sincere.

Our Edge
• One-Stop Logistics Solutions
• Extensive Network Throughout Malaysia
• Highly Qualified and Experienced Pool of Professionals
• Comprehensive IT Solutions
• Innovative and Customer-focused Solutions
• Flexible and Consistent in Managing Exceptions
• Total Supply Chain Visibility

Target Market(s)

We sell the logistics services to all the industry in Malaysia. (ONE Stop Logistics Solutions)

Industry/Entity Type

Logistic

Contact Information for Business Card

I want the back of the card to be white with the logo and slogan. i would like to see the logo on the front with the general info.

Requirements
Must have
• Name, Title, Office, Cell, Fax, Email, Address, Website
Nice to have
• Modern Design Business Card

```html
<!DOCTYPE html>
<html lang="en">
<head>
<meta charset="utf-8">
<title>Harrowmere Logistics – Stationery</title>
<link href="https://fonts.googleapis.com/css2?family=Roboto:wght@400;500;700&family=Roboto+Condensed:wght@700&display=swap" rel="stylesheet">
<style>
  :root{
    --canvas:#cdcdcd;
    --paper:#f7f7f7;
    --blue:#3a7bc8;
    --blue-dark:#2f64a3;
    --ink:#333;
    --grey-band-a:#e2e2e2;
    --grey-band-b:#555;
    --folder-top:#3698d7;
    --folder-bottom:#2f5ea8;
  }
  *{box-sizing:border-box;margin:0;padding:0}
  html,body{width:1198px;height:1200px;overflow:hidden}
  body{background:var(--canvas);position:relative;font-family:"Roboto",Arial,sans-serif;color:var(--ink)}
  .sheet{position:absolute;background:var(--paper);overflow:hidden;box-shadow:0 1px 3px rgba(0,0,0,.18)}

  /* shared brand name block */
  .brand{position:absolute;display:flex;align-items:center;gap:5px;color:var(--blue);font-weight:500;line-height:1.05}
  .brand-dot{border-radius:50%;background:var(--blue);flex:none}
  .brand-name{display:block}

  /* footer band */
  .band{position:absolute;left:0;right:0;bottom:0;background:linear-gradient(90deg,var(--grey-band-a),var(--grey-band-b))}
  .band-tag{position:absolute;right:0;top:0;bottom:0;background:var(--blue-dark);color:#fff;font-weight:700;display:flex;align-items:center;letter-spacing:.3px;clip-path:polygon(9% 0,100% 0,100% 100%,0 100%)}

  /* letterhead */
  .letterhead{left:89px;top:49px;width:484px;height:685px}
  .company-title{position:absolute;left:32px;top:42px;font-family:"Roboto Condensed",Arial,sans-serif;font-weight:700;font-size:10.5px;color:var(--blue-dark)}
  .company-no{position:absolute;left:32px;top:56px;font-size:7.5px}
  .contact-list{position:absolute;left:32px;top:72px;list-style:none;font-size:6.8px;line-height:9px}
  .contact-list li{display:flex;align-items:center;gap:5px}
  .ico{width:7px;height:7px;flex:none}
  .gst{position:absolute;left:32px;top:112px;font-size:7px;color:var(--blue);font-weight:500}
  .letterhead .brand{left:355px;top:88px;font-size:14px;width:110px}
  .letterhead .brand-dot{width:9px;height:9px}
  .address{position:absolute;font-size:7px;line-height:10px}
  .letterhead .address{left:32px;top:640px}
  .letterhead .band{height:17px}
  .letterhead .band-tag{width:208px;font-size:7px;padding-left:38px}

  /* folder */
  .folder{left:625px;top:49px;width:485px;height:685px;background:linear-gradient(180deg,var(--folder-top),var(--folder-bottom))}
  .folder-crease{position:absolute;top:0;bottom:0;width:1px;background:rgba(20,60,120,.45)}
  .folder .brand{left:0;right:0;top:370px;justify-content:center;color:#fff;font-size:27px;font-weight:400;text-align:center;flex-direction:column;gap:10px}
  .folder .brand-dot{width:14px;height:14px;background:#fff}

  /* envelopes */
  .env-back{left:170px;top:773px;width:591px;height:264px;background:#fff}
  .env-flap{position:absolute;left:0;top:0;width:591px;height:88px}
  .env-url{position:absolute;left:0;right:0;top:42px;text-align:center;color:#fff;font-size:7.5px;letter-spacing:.4px}
  .env-front{left:121px;top:885px;width:586px;height:265px}
  .env-front .brand{left:30px;top:36px;font-size:12px;width:90px}
  .env-front .brand-dot{width:8px;height:8px}
  .env-front .address{left:29px;top:219px}
  .env-front .band{height:13px}
  .env-front .band-tag{width:215px;font-size:7px;padding-left:44px}

  /* business cards */
  .card{left:868px;width:209px;height:127px}
  .card-services{top:797px}
  .card-contact{top:963px}
  .card .brand{left:128px;font-size:11px;width:76px}
  .card .brand-dot{width:6px;height:6px}
  .card-services .brand{top:42px}
  .card-contact .brand{top:20px}
  .card .band{height:12px}
  .card .band-tag{width:122px;font-size:5.2px;padding-left:21px}
  .services-title{position:absolute;left:14px;top:15px;font-family:"Roboto Condensed",Arial,sans-serif;font-weight:700;font-size:6.5px;color:var(--blue-dark)}
  .services-list{position:absolute;left:14px;top:29px;list-style:none;font-size:4.6px;line-height:8px}
  .services-list li::before{content:"» ";color:var(--blue)}
  .holder{position:absolute;left:10px;top:12px;border-left:2px solid var(--blue-dark);padding-left:9px}
  .holder-name{font-family:"Roboto Condensed",Arial,sans-serif;font-weight:700;font-size:7px;color:var(--blue-dark)}
  .holder-role{font-size:4.6px;line-height:7px}
  .holder-cell{font-size:4.8px;font-weight:700}
  .card-company{position:absolute;left:10px;top:56px;font-family:"Roboto Condensed",Arial,sans-serif;font-weight:700;font-size:6px;color:var(--blue-dark)}
  .card-company-no{position:absolute;left:10px;top:64px;font-size:4.3px}
  .card-details{position:absolute;left:10px;top:76px;list-style:none;font-size:4.6px;line-height:7px}
  .card-details li{display:flex;gap:4px}
  .card-details .web{color:var(--blue)}
</style>
</head>
<body>

<!-- Letterhead -->
<section class="sheet letterhead" aria-label="Letterhead">
  <h1 class="company-title">HARROWMERE LOGISTICS SDN. BHD.</h1>
  <p class="company-no">(Company No. 1046283-K)</p>
  <ul class="contact-list">
    <li><svg class="ico" viewBox="0 0 10 10"><path d="M2 1h2l1 2-1 1a6 6 0 0 0 2 2l1-1 2 1v2a1 1 0 0 1-1 1A8 8 0 0 1 1 2a1 1 0 0 1 1-1z" fill="var(--blue-dark)"/></svg>(603) 5521 3840 / 3850</li>
    <li><svg class="ico" viewBox="0 0 10 10"><rect x="1" y="4" width="8" height="4" fill="var(--blue-dark)"/><rect x="3" y="1" width="4" height="3" fill="var(--blue-dark)"/></svg>(603) 5521 3860</li>
    <li><svg class="ico" viewBox="0 0 10 10"><rect x="1" y="2" width="8" height="6" fill="var(--blue-dark)"/><path d="M1 2l4 3 4-3" stroke="#fff" fill="none"/></svg>farid.hakimi@harrowmere.com.my</li>
    <li><svg class="ico" viewBox="0 0 10 10"><circle cx="5" cy="5" r="4" fill="none" stroke="var(--blue-dark)"/><path d="M1 5h8M5 1v8" stroke="var(--blue-dark)"/></svg>www.harrowmere.com.my</li>
  </ul>
  <p class="gst">GST Registration No: 000184520719</p>
  <div class="brand"><span class="brand-dot"></span><span class="brand-name">Harrowmere Logistics</span></div>
  <p class="address">No. 14B, 2nd Floor, Jalan Seroja 3, Taman Seroja,<br>41050 Klang, Selangor Darul Ehsan, Malaysia.</p>
  <div class="band"><div class="band-tag">ONE STOP LOGISTICS SOLUTIONS</div></div>
</section>

<!-- Presentation folder -->
<section class="sheet folder" aria-label="Presentation folder">
  <span class="folder-crease" style="left:33px"></span>
  <span class="folder-crease" style="left:40px"></span>
  <div class="brand"><span class="brand-dot"></span><span class="brand-name">Harrowmere Logistics</span></div>
</section>

<!-- Envelope back -->
<section class="sheet env-back" aria-label="Envelope back">
  <svg class="env-flap" viewBox="0 0 591 88" preserveAspectRatio="none">
    <path d="M6 0H591L557 42Q530 88 505 88H80Q52 88 35 42Z" fill="var(--blue-dark)"/>
  </svg>
  <p class="env-url">www.harrowmere.com.my</p>
</section>

<!-- Envelope front -->
<section class="sheet env-front" aria-label="Envelope front">
  <div class="brand"><span class="brand-dot"></span><span class="brand-name">Harrowmere Logistics</span></div>
  <p class="address">No. 14B, 2nd Floor, Jalan Seroja 3, Taman Seroja,<br>41050 Klang, Selangor Darul Ehsan, Malaysia.</p>
  <div class="band"><div class="band-tag">ONE STOP LOGISTICS SOLUTIONS</div></div>
</section>

<!-- Business card: services side -->
<section class="sheet card card-services" aria-label="Business card services side">
  <h2 class="services-title">We're Specialize In</h2>
  <ul class="services-list">
    <li>International Shipping (Air / Sea)</li>
    <li>Consolidation: NVOCC</li>
    <li>Project Management</li>
    <li>Supply Chain Management</li>
    <li>Tax Exemption Consultancy</li>
    <li>Custom Brokerage</li>
    <li>Transportation / Haulage</li>
    <li>Warehousing</li>
    <li>Packing &nbsp;» Marine Insurance</li>
    <li>Distribution &nbsp;» Door to Door</li>
  </ul>
  <div class="brand"><span class="brand-dot"></span><span class="brand-name">Harrowmere Logistics</span></div>
  <div class="band"><div class="band-tag">ONE STOP LOGISTICS SOLUTIONS</div></div>
</section>

<!-- Business card: contact side -->
<section class="sheet card card-contact" aria-label="Business card contact side">
  <div class="holder">
    <p class="holder-name">Farid Hakimi</p>
    <p class="holder-role">Managing Director</p>
    <p class="holder-cell">+6012-418 2275</p>
  </div>
  <div class="brand"><span class="brand-dot"></span><span class="brand-name">Harrowmere Logistics</span></div>
  <p class="card-company">HARROWMERE LOGISTICS SDN. BHD.</p>
  <p class="card-company-no">(Company No. 1046283-K)</p>
  <ul class="card-details">
    <li>(603) 5521 3840 / 3850</li>
    <li>(603) 5521 3860</li>
    <li>farid.hakimi@harrowmere.com.my <span class="web">www.harrowmere.com.my</span></li>
    <li>No. 14B, 2nd Floor, Jalan Seroja 3, Taman Seroja, 41050 Klang,</li>
    <li>Selangor Darul Ehsan, Malaysia.</li>
  </ul>
  <div class="band"><div class="band-tag">ONE STOP LOGISTICS SOLUTIONS</div></div>
</section>

</body>
</html>
```